Graphic Design Project

I need to create a graphic design, which needs to be editable for me in Powerpoint... I have attached it a draft of it, but I need to be able to change the text of it. I want it to look more professional
Updates

Target Market(s)

Business Executives

Industry/Entity Type

Graphic Design

Requirements
Must have
• Make it look professional; the colors can change; I just need to be able to edit the text in powerpoint or either word

```html
<!DOCTYPE html>
<html lang="en">
<head>
<meta charset="UTF-8">
<title>Managing IT Change – Roadmap</title>
<link rel="stylesheet" href="https://fonts.googleapis.com/css2?family=Arimo:wght@400;700&display=swap">
<style>
  :root {
    --canvas-bg: #e6dfd1;
    --canvas-bg-light: #ece6da;
    --rail-dark: #a50d12;
    --rail-light: #ec6a6a;
    --rail-edge: #6f8fc8;
    --box-dark: #b0121a;
    --box-mid: #d63a3f;
    --box-light: #ee7373;
    --connector: #c0393c;
    --label: #ffffff;
  }
  * { box-sizing: border-box; margin: 0; padding: 0; }
  html, body { width: 1200px; height: 665px; overflow: hidden; }
  body {
    position: relative;
    background: radial-gradient(ellipse at 60% 45%, var(--canvas-bg-light), var(--canvas-bg));
    font-family: "Arimo", Arial, sans-serif;
  }
  .side-rail {
    position: absolute; left: 0; top: 0; width: 91px; height: 665px;
    background: linear-gradient(to bottom, var(--rail-dark), var(--rail-light));
    border-left: 3px solid var(--rail-edge);
  }
  .connectors { position: absolute; inset: 0; width: 1200px; height: 665px; }
  .step {
    position: absolute;
    display: flex; align-items: center; justify-content: center;
    text-align: center;
    color: var(--label);
    font-size: 22px; line-height: 1.18;
    padding: 0 12px;
    background: radial-gradient(ellipse 70% 75% at 50% 65%, var(--box-light) 0%, var(--box-mid) 50%, var(--box-dark) 100%);
    box-shadow: 3px 4px 7px rgba(0,0,0,0.45);
  }
  .step--lead { font-size: 31px; text-shadow: 1px 2px 3px rgba(0,0,0,0.55); }
</style>
</head>
<body>
  <div class="side-rail"></div>

  <svg class="connectors" viewBox="0 0 1200 665" aria-hidden="true">
    <defs>
      <marker id="arrowhead" markerWidth="12" markerHeight="12" refX="11" refY="6" orient="auto" markerUnits="userSpaceOnUse">
        <path d="M1,1 L11,6 L1,11" fill="none" stroke="#c0393c" stroke-width="1.4"/>
      </marker>
    </defs>
    <g fill="none" stroke="var(--connector)" stroke-width="1.4" marker-end="url(#arrowhead)">
      <line x1="362" y1="138" x2="411" y2="138"/>
      <line x1="640" y1="138" x2="687" y2="138"/>
      <polyline points="803,207 803,238 230,238 230,267"/>
      <line x1="344" y1="337" x2="391" y2="337"/>
      <line x1="620" y1="337" x2="668" y2="337"/>
      <line x1="898" y1="337" x2="945" y2="337"/>
      <polyline points="1060,406 1060,431 230,431 230,454"/>
      <line x1="344" y1="524" x2="391" y2="524"/>
      <line x1="620" y1="524" x2="668" y2="524"/>
      <line x1="898" y1="524" x2="945" y2="524"/>
    </g>
  </svg>

  <div class="step step--lead" style="left:118px;top:60px;width:243px;height:157px;">MANAGING</div>
  <div class="step" style="left:415px;top:70px;width:224px;height:136px;">Maintain IT<br>Operational<br>Excellence<br>CHANGE</div>
  <div class="step" style="left:690px;top:70px;width:225px;height:136px;">Create Business<br>Value</div>

  <div class="step" style="left:118px;top:270px;width:225px;height:135px;">Transform IT<br>Team</div>
  <div class="step" style="left:394px;top:270px;width:225px;height:135px;">Master<br>Relationship<br>Management</div>
  <div class="step" style="left:671px;top:270px;width:226px;height:135px;">Market &amp;<br>Communicate<br>Value</div>
  <div class="step" style="left:948px;top:270px;width:225px;height:135px;">Customer<br>Engagement<br>Model</div>

  <div class="step" style="left:118px;top:457px;width:225px;height:135px;">Service-Minded</div>
  <div class="step" style="left:394px;top:457px;width:225px;height:135px;">IT Culture</div>
  <div class="step" style="left:671px;top:457px;width:226px;height:135px;">Policy, Process &amp;<br>Methodologies</div>
  <div class="step" style="left:948px;top:457px;width:225px;height:135px;">Meaningful<br>Metrics</div>
</body>
</html>
```